Trade Show booth design

I need the following designs for my trade booth:
1. backboard design 3m Wx2mH
2. Tressle table, tablecloth front panel design 1800W x 740mmH
3. Pop-up banner. I have included our logos and some design content ideas:
Headline:
"Cleaner Classrooms. Safer Schools."
Subheadline:
"Specialist Cleaning Solutions for Education Facilities"
Key Points to Grab Attention:
Healthy Environments: Create hygienic, safe learning spaces for students and staff with our expert cleaning services.
Tailored to Your Needs: Custom cleaning plans for classrooms, labs, libraries, and sports facilities.
Affordable Excellence: Premium results without premium costs – tailored plans mean you only pay for what you need.
Safety First: All staff are trained, highly vetted, and hold current Working with Children Checks (WWCC).
Eco-Conscious Cleaning: Using non-toxic, eco-friendly products certified for health and safety.
What Schools Really Need:
Reliability: Consistent, high-quality cleaning from a trusted provider.
Cost-Effectiveness: Solutions that fit tight budgets while maintaining high standards.
Expertise: Over 30 years of experience in education facility cleaning.
Disinfection Services: Focus on high-touch areas to reduce the spread of germs and ensure peace of mind.
Visual Elements:
Images of bright, clean classrooms, a happy teacher welcoming students, or students collaborating in a spotless library.
Icons representing safety (shield), hygiene (sparkling star), and eco-friendliness (leaf).
Your logo with the tagline: "Trusted by Queensland Schools Since 1995."
Call-to-Action:
"Visit us to discuss your school’s cleaning needs and book a FREE consultation."
Include contact details: Phone: 1300 649 315 | Website: www.duravoss.com.au
Target Market(s)
Education sector
Industry/Entity Type
Commercial Cleaning
Font styles to use
Other font styles liked:
- Montserrat
Look and feel

```html
<!DOCTYPE html>
<html lang="en">
<head>
<meta charset="utf-8">
<title>Duravoss – Education Cleaning Backboard</title>
<link rel="stylesheet" href="https://fonts.googleapis.com/css2?family=Montserrat:wght@400;500;600;700;800&display=swap">
<style>
  :root {
    --navy: #1f3f66;
    --blue: #2b8be0;
    --ink: #1b1b1b;
    --paper: #ffffff;
    --backdrop: #e6e8eb;
  }
  * { margin: 0; padding: 0; box-sizing: border-box; }
  html, body { width: 1200px; height: 1200px; overflow: hidden; }
  body { background: var(--backdrop); font-family: "Montserrat", sans-serif; position: relative; }

  .board {
    position: absolute; left: 30px; top: 218px;
    width: 1140px; height: 763px;
    background: var(--paper);
    box-shadow: 0 12px 30px rgba(0,0,0,.18);
    overflow: hidden;
  }

  .brand { position: absolute; left: 57px; top: 30px; }
  .brand-name {
    display: flex; align-items: center; gap: 16px;
    font-weight: 800; font-size: 62px; letter-spacing: -1px;
    color: var(--navy); line-height: 1;
  }
  .brand-dot { width: 40px; height: 40px; border-radius: 50%; background: var(--navy); }
  .brand-tagline {
    position: absolute; left: 57px; top: 146px;
    font-size: 16px; font-weight: 400; color: var(--ink); letter-spacing: .1px; white-space: nowrap;
  }

  .headline { position: absolute; left: 577px; top: 22px; color: var(--navy); }
  .headline h1 { font-size: 32px; font-weight: 700; line-height: 42px; letter-spacing: -.2px; }
  .headline p { font-size: 26px; font-weight: 400; line-height: 34px; color: var(--ink); margin-top: 2px; white-space: nowrap; }

  .band { position: absolute; left: 0; top: 198px; width: 100%; height: 111px; background: var(--navy); }
  .band-stripe { position: absolute; left: 0; top: 309px; width: 100%; height: 6px; background: var(--blue); }

  .photo { position: absolute; top: 226px; width: 340px; height: 204px; }
  .photo-classroom { left: 52px; background: linear-gradient(135deg, #e6a03a 0%, #c98a4a 45%, #6f7f92 100%); }
  .photo-welcome { left: 400px; background: linear-gradient(135deg, #8a4b2a 0%, #c07a45 50%, #a45a34 100%); }
  .photo-library { left: 747px; background: linear-gradient(135deg, #7c4a2c 0%, #b8a68a 45%, #3f5f86 100%); }

  .feature { position: absolute; top: 447px; width: 300px; text-align: center; }
  .feature svg { display: block; margin: 0 auto; }
  .feature p { margin-top: 8px; font-size: 15.5px; font-weight: 600; line-height: 20px; color: var(--ink); white-space: nowrap; letter-spacing: -.2px; }
  .feature p strong { color: var(--blue); font-weight: 700; }
  .feature-expertise { left: 146px; }
  .feature-trust { left: 441px; }
  .feature-eco { left: 723px; }

  .cta { position: absolute; left: 0; top: 657px; width: 100%; text-align: center; font-size: 18px; font-weight: 600; color: var(--navy); letter-spacing: -.2px; }
  .cta strong { font-weight: 800; }

  .contact {
    position: absolute; left: 175px; top: 688px; width: 778px; height: 54px;
    background: var(--navy); color: #fff;
    display: flex; align-items: center; justify-content: center; gap: 10px;
    font-size: 35px; font-weight: 800; letter-spacing: -.5px;
  }
  .contact svg { flex: none; }
  .contact .divider { font-weight: 700; margin: 0 4px; }
</style>
</head>
<body>
  <main class="board">
    <div class="brand">
      <div class="brand-name"><span class="brand-dot"></span>duravoss</div>
    </div>
    <div class="brand-tagline">TRUSTED BY QUEENSLAND SCHOOLS SINCE 1995</div>

    <header class="headline">
      <h1>Creating Cleaner,<br>Safer Learning Environments</h1>
      <p>Specialists in Education<br>Facility Cleaning &amp; Eco-Friendly Services</p>
    </header>

    <div class="band"></div>
    <div class="band-stripe"></div>

    <div class="photo photo-classroom" role="img" aria-label="Bright classroom with a teacher and students working at laptops"></div>
    <div class="photo photo-welcome" role="img" aria-label="Teacher greeting young students with high fives at the classroom door"></div>
    <div class="photo photo-library" role="img" aria-label="Students collaborating between bookshelves in a tidy library"></div>

    <section class="feature feature-expertise">
      <svg width="140" height="150" viewBox="0 0 140 150" fill="none" stroke="var(--navy)" stroke-width="2.6" stroke-linecap="round" stroke-linejoin="round">
        <circle cx="70" cy="66" r="64"/>
        <path d="M60 136 L70 146 L80 136" fill="var(--navy)" stroke="none"/>
        <circle cx="70" cy="54" r="24"/>
        <circle cx="70" cy="54" r="16"/>
        <path d="M70 45 l3 6 6.5 .8 -4.8 4.4 1.3 6.4 -6 -3.3 -6 3.3 1.3 -6.4 -4.8 -4.4 6.5 -.8z"/>
        <path d="M56 74 L46 96 L55 93 L59 101 L66 80"/>
        <path d="M84 74 L94 96 L85 93 L81 101 L74 80"/>
      </svg>
      <p>Over <strong>30 years of expertise</strong> in<br>commercial cleaning</p>
    </section>

    <section class="feature feature-trust">
      <svg width="140" height="150" viewBox="0 0 140 150" fill="none" stroke="var(--navy)" stroke-width="2.6" stroke-linecap="round" stroke-linejoin="round">
        <circle cx="70" cy="66" r="64"/>
        <path d="M60 136 L70 146 L80 136" fill="var(--navy)" stroke="none"/>
        <path d="M70 20 L86 26 V40 C86 52 78 58 70 62 C62 58 54 52 54 40 V26 Z"/>
        <path d="M62 40 L68 46 L79 34"/>
        <path d="M34 78 L46 66 L60 74 L72 70 L84 72 L94 66 L106 78 L96 90"/>
        <path d="M44 86 L58 98 C62 101 66 101 70 98 L86 86"/>
        <path d="M60 80 L70 76 L84 88"/>
      </svg>
      <p>Trusted by <strong>schools, universities,</strong><br><strong>and TAFEs</strong> across Queensland</p>
    </section>

    <section class="feature feature-eco">
      <svg width="140" height="150" viewBox="0 0 140 150" fill="none" stroke="var(--navy)" stroke-width="2.6" stroke-linecap="round" stroke-linejoin="round">
        <circle cx="70" cy="66" r="64"/>
        <path d="M60 136 L70 146 L80 136" fill="var(--navy)" stroke="none"/>
        <circle cx="43" cy="42" r="10" fill="var(--navy)"/>
        <path d="M38 42 l4 4 7 -7" stroke="#fff"/>
        <circle cx="43" cy="72" r="10" fill="var(--navy)"/>
        <path d="M38 72 l4 4 7 -7" stroke="#fff"/>
        <path d="M60 37 H92 M60 48 H88 M60 68 H74" stroke-width="4"/>
        <path d="M66 104 C66 82 80 70 106 68 C104 90 92 102 72 102 Z" fill="var(--navy)"/>
        <path d="M64 108 L90 82" stroke="#fff" stroke-width="2"/>
      </svg>
      <p>100% <strong>Carbon Neutral and</strong><br><strong>Eco-Certified</strong> Services</p>
    </section>

    <p class="cta">Visit us to discuss your school’s cleaning needs and book a <strong>FREE</strong> consultation</p>

    <div class="contact">
      <svg width="28" height="32" viewBox="0 0 28 32" fill="none" stroke="var(--blue)" stroke-width="2.6" stroke-linecap="round" stroke-linejoin="round">
        <path d="M7 3 L12 9 L9 13 C10 18 13 22 17 24 L21 21 L26 26 L22 30 C12 29 3 19 3 8 Z" fill="var(--blue)"/>
        <path d="M16 9 a6 6 0 0 1 5 5 M17 4 a11 11 0 0 1 9 9"/>
      </svg>
      <span>1300 649 315</span>
      <span class="divider">|</span>
      <svg width="32" height="32" viewBox="0 0 32 32" fill="none" stroke="var(--blue)" stroke-width="2" stroke-linecap="round">
        <circle cx="15" cy="15" r="12"/>
        <ellipse cx="15" cy="15" rx="5.5" ry="12"/>
        <path d="M3 15 H27 M5 9 H25 M5 21 H20"/>
        <path d="M20 20 L30 24 L25.5 25.5 L24 30 Z" fill="var(--blue)"/>
      </svg>
      <span>www.duravoss.com.au</span>
    </div>
  </main>
</body>
</html>
```